Re-design of current business cards

We are updating our website with new colors and layout. Would like to re-design our business cards to co-ordinate. See attached pdf with new Fernbrook website colors. We would also like to combine our 2 brands on the one business card. Attached is the new design for our Fernbrook website, current business cards, which are one sided, fernbrook logo in tiff, .ai for fonts. Fernbrook logo font is Optimum, Lanternfield website home page image, Lanternfield brand statics for products which includes the logo for this brand.

Lanternfield brand will stay the dark gray on the website. See attached statics for product and website home page.
Updates

The business cards will be 2 sided. Fernbrook Brand on one side and Lanternfield Brand on the other. The colors for Fernbrook need to follow the color scheme of the fernbrook website pdf I uploaded. The colors are a blue, lighter teal blue and white. Lanternfield needs to follow the dark gray color on files uploaded

Target Market(s)

The trade and consumers

Industry/Entity Type

Home Furnishing

Contact Information for Business Card

We are updating our website with new colors and layout. Would like to re-design our business cards to co-ordinate. We would also like to combine our 2 brands onto 1 2 sided business cards.

Requirements
Must have
• Colors that match our new website, see attached image.
• RGB colors
• navy -#152842
• teal - 98aeb9
• The gray color used for Lanternfield brands.
• ll logos and fonts should stay the same.

```html
<!DOCTYPE html>
<html lang="en">
<head>
<meta charset="utf-8">
<title>Fernbrook &amp; Lanternfield Business Cards</title>
<link href="https://fonts.googleapis.com/css2?family=Belleza&family=Cormorant+Garamond:wght@500&family=Roboto+Condensed:wght@600&family=Roboto:wght@400&display=swap" rel="stylesheet">
<style>
  :root {
    --backdrop: #e6e7ea;
    --navy: #152842;
    --slate: #5a5b5e;
    --slate-dark: #4c4d50;
    --white: #ffffff;
    --paper: #fbfbfc;
    --ink-soft: #2a3446;
  }
  * { margin: 0; padding: 0; box-sizing: border-box; }
  html, body { width: 1200px; height: 864px; overflow: hidden; background: var(--backdrop); }
  .sheet {
    width: 1200px; height: 864px;
    display: flex; flex-direction: column; align-items: center; justify-content: center; gap: 56px;
  }
  .card {
    position: relative; width: 620px; height: 354px; border-radius: 22px; overflow: hidden;
    box-shadow: 0 10px 30px rgba(0,0,0,.18);
  }

  /* Lanternfield side */
  .card--lanternfield {
    background: linear-gradient(160deg, var(--slate) 0%, var(--slate-dark) 100%);
    color: var(--white); text-align: center;
  }
  .brand-lockup { position: absolute; top: 96px; left: 0; right: 0; }
  .brand-name {
    font-family: "Cormorant Garamond", Georgia, serif; font-weight: 500;
    font-size: 54px; letter-spacing: 1px; line-height: 1;
  }
  .brand-by {
    font-family: "Cormorant Garamond", Georgia, serif; font-weight: 500;
    font-size: 13px; letter-spacing: 1px; text-align: right; padding-right: 108px; margin-top: 2px;
  }
  .tagline {
    position: absolute; top: 222px; left: 0; right: 0;
    font-family: "Roboto Condensed", Arial, sans-serif; font-weight: 600;
    font-size: 17px; letter-spacing: 5px;
  }
  .site-url {
    position: absolute; top: 252px; left: 0; right: 0;
    font-family: Roboto, Arial, sans-serif; font-size: 13px; letter-spacing: .3px; opacity: .92;
  }

  /* Fernbrook side */
  .card--fernbrook { background: var(--paper); color: var(--navy); font-family: Belleza, "Trebuchet MS", sans-serif; }
  .card-frame { position: absolute; inset: 0; }
  .logo { position: absolute; top: 92px; left: 150px; display: flex; align-items: center; gap: 12px; }
  .logo-dot { width: 34px; height: 34px; border-radius: 50%; background: var(--navy); }
  .logo-name { font-size: 50px; letter-spacing: 2px; line-height: 1; }
  .contacts { position: absolute; top: 46px; left: 420px; list-style: none; font-size: 12.5px; color: var(--ink-soft); }
  .contacts li { display: flex; align-items: center; gap: 7px; height: 17px; }
  .contacts svg { width: 10px; height: 10px; fill: var(--navy); }
  .person { position: absolute; top: 208px; left: 28px; }
  .person-name { font-size: 20px; letter-spacing: .5px; }
  .person-title { font-size: 13.5px; color: var(--ink-soft); letter-spacing: .3px; }
  .address { position: absolute; top: 280px; left: 28px; font-family: "Cormorant Garamond", Georgia, serif; font-size: 14px; color: var(--ink-soft); }
  .band-url {
    position: absolute; bottom: 8px; right: 40px; color: var(--white);
    font-family: Roboto, Arial, sans-serif; font-size: 11px; letter-spacing: 4px;
  }
</style>
</head>
<body>
<main class="sheet">

  <section class="card card--lanternfield" aria-label="Lanternfield side">
    <div class="brand-lockup">
      <div class="brand-name">LANTERNFIELD</div>
      <div class="brand-by">by FERNBROOK</div>
    </div>
    <p class="tagline">DISCOVER THE LUXURY OF HOME</p>
    <p class="site-url">www.Lanternfieldbyfernbrook.com</p>
  </section>

  <section class="card card--fernbrook" aria-label="Fernbrook side">
    <svg class="card-frame" viewBox="0 0 620 354" aria-hidden="true">
      <line x1="250" y1="36" x2="590" y2="36" stroke="#152842" stroke-width="1"/>
      <line x1="26" y1="196" x2="330" y2="196" stroke="#152842" stroke-width="1"/>
      <polygon points="206,354 232,328 600,328 600,48 620,48 620,354" fill="#152842"/>
      <polyline points="190,344 220,316 590,316 590,44 596,36" fill="none" stroke="#152842" stroke-width="2"/>
    </svg>

    <div class="logo">
      <span class="logo-dot"></span>
      <span class="logo-name">FERNBROOK</span>
    </div>

    <ul class="contacts">
      <li><svg viewBox="0 0 10 10"><path d="M2 0.5 3.6 2.6 2.6 3.6C3.2 5 5 6.8 6.4 7.4L7.4 6.4 9.5 8 8.3 9.5C4.5 9.2 0.8 5.5 0.5 1.7Z"/></svg>555.201.4830</li>
      <li><svg viewBox="0 0 10 10"><path d="M2.5 0.5h5v2.5h-5zM0.5 3.5h9v4h-2v2h-5v-2h-2z"/></svg>555.201.4871</li>
      <li><svg viewBox="0 0 10 10"><path d="M0.5 2h9v6h-9zM0.5 2 5 5.5 9.5 2" stroke="#fff" stroke-width=".6"/></svg>dwhitlow@fernbrook.com</li>
    </ul>

    <div class="person">
      <p class="person-name">DANA WHITLOW</p>
      <p class="person-title">GRAPHICS/PHOTOGRAPHY DIRECTOR</p>
    </div>
    <p class="address">Po box 412/1870 meadow run rd, Cedar falls, Ohio 45012</p>
    <p class="band-url">WWW.FERNBROOK.COM</p>
  </section>

</main>
</body>
</html>
```